label for a line of bbq rubs. my competition team name is copper kettle bbq *

i already have a logo, just need a label designed for a line of bbq rubs im developing. i want the design to be clean and eye catching and my colors of my logo are black and white. these will be sold in bbq specialty stores. i have a lot of traction in the bbq competition community, they are all familiar with my logo, just need a design that will stand out and draw attention to buys online and in the stores

Target Market(s)

backyard bbq cooks

Industry/Entity Type

Food blog

Font styles to use
Sans Serif

Colors

Designer to choose only greyscale colors for use in the design.

Requirements
Must have
• project must be simple, clean, with a classic look
Nice to have
• my logo, clean and simple

i have include some examples from other companies
Should not have
• cartoons

```html
<!DOCTYPE html>
<html lang="en">
<head>
<meta charset="utf-8">
<title>Copper Kettle BBQ – Barbeque Rub Labels</title>
<link href="https://fonts.googleapis.com/css2?family=Oswald:wght@400;600;700&family=Roboto+Condensed:wght@400;700&family=Courier+Prime:wght@700&display=swap" rel="stylesheet">
<style>
:root{
  --ink:#000;
  --label:#050505;
  --front:#3b3b3d;
  --paper:#fff;
  --soft:#e9e9e9;
  --mute:#bdbdbd;
  --silhouette:#f2f2f2;
}
*{box-sizing:border-box;margin:0;padding:0}
html,body{width:1200px;height:1000px;overflow:hidden;background:var(--paper)}
.canvas{position:relative;width:1200px;height:1000px;background:var(--paper)}
.stage-dark{position:absolute;left:0;top:0;width:600px;height:1000px;background:var(--ink)}

/* front panel */
.front{position:absolute;left:123px;top:275px;width:347px;height:540px;background:var(--front);color:var(--paper);text-align:center}
.front .brand-tab{left:113px;top:-32px;width:126px;height:124px;font-size:24px}
.front .title{position:absolute;left:0;right:0;top:142px;font:700 80px/1 "Oswald",sans-serif;letter-spacing:4px;text-shadow:4px 4px 0 #777}
.front .title .dot{font-size:22px;vertical-align:middle;margin:0 14px;text-shadow:none}
.front .subtitle{position:absolute;left:0;right:0;top:252px;font:400 31px/1 "Oswald",sans-serif;letter-spacing:2px}
.front .animal{position:absolute;left:90px;top:332px;width:175px;height:118px;background:var(--silhouette);border-radius:6px}
.front .rule{position:absolute;left:92px;right:92px;top:490px;border-top:2px solid var(--mute)}
.front .volume{position:absolute;left:0;right:0;top:502px;font:400 13px/1 "Oswald",sans-serif}
.front .quote-end{position:absolute;left:22px;top:392px;font:700 28px/1 "Oswald",sans-serif}

/* flat labels */
.label{position:absolute;left:693px;width:474px;background:var(--label);color:var(--paper);box-shadow:0 2px 6px rgba(0,0,0,.25)}
.label-chicken{top:77px;height:256px}
.label-pig{top:365px;height:284px}
.label-beef{top:676px;height:282px}

.brand-tab{position:absolute;left:185px;top:-30px;width:70px;height:58px;background:var(--paper);border-radius:5px;display:flex;align-items:center;justify-content:center;text-align:center;color:var(--ink);font:700 12px/1.05 "Oswald",sans-serif;letter-spacing:.5px}
.emblem{position:absolute;left:40px;top:12px;width:54px;height:40px;background:var(--silhouette);border-radius:4px}
.story{position:absolute;left:22px;top:70px;width:118px;font:700 5.6px/1.75 "Courier Prime",monospace;text-align:center}
.story .q{position:absolute;font:700 20px/1 "Oswald",sans-serif}
.story .q-open{left:-8px;top:-6px}
.story .q-close{right:-10px;bottom:-8px}
.follow{position:absolute;left:38px;bottom:22px;display:flex;align-items:center;gap:4px;font:600 8px/1 "Oswald",sans-serif;letter-spacing:.4px}
.follow .dot{width:8px;height:8px;border-radius:50%;background:var(--paper)}
.label .title{position:absolute;left:140px;width:180px;text-align:center;font:700 30px/1 "Oswald",sans-serif;letter-spacing:2px;text-shadow:2px 2px 0 #777}
.label .title .dot{font-size:9px;vertical-align:middle;margin:0 5px;text-shadow:none}
.label .subtitle{position:absolute;left:140px;width:180px;text-align:center;font:400 15px/1 "Oswald",sans-serif;letter-spacing:1px}
.label .animal{position:absolute;background:var(--silhouette);border-radius:4px}
.label .rule{position:absolute;left:170px;width:118px;border-top:1px solid var(--mute)}
.label .volume{position:absolute;left:140px;width:180px;text-align:center;font:400 8px/1 "Oswald",sans-serif}

.nutrition{position:absolute;left:324px;top:20px;width:141px;background:var(--paper);color:var(--ink);padding:2px 3px;font:400 5px/1.25 "Roboto Condensed",sans-serif}
.nutrition h3{font:700 10px/1 "Roboto Condensed",sans-serif;border-bottom:1px solid var(--ink);padding-bottom:1px}
.nutrition .thick{border-bottom:3px solid var(--ink)}
.nutrition .cal{display:flex;justify-content:space-between;font:700 9px/1.1 "Roboto Condensed",sans-serif;border-bottom:2px solid var(--ink)}
.nutrition .row{display:flex;justify-content:space-between;border-bottom:.5px solid #666}
.nutrition .in{padding-left:6px}
.nutrition .dv{text-align:right;border-bottom:.5px solid #666}
.nutrition .foot{font-size:4px;line-height:1.3;padding-top:1px}
</style>
</head>
<body>
<main class="canvas">
  <section class="stage-dark">
    <div class="front">
      <div class="brand-tab">COPPER<br>KETTLE<br>BBQ</div>
      <div class="title"><span class="dot">■</span>BEEF<span class="dot">■</span></div>
      <div class="subtitle">BARBEQUE RUB</div>
      <div class="animal" role="img" aria-label="White silhouette of a cow"></div>
      <div class="quote-end">”</div>
      <div class="rule"></div>
      <div class="volume">250ml</div>
    </div>
  </section>

  <article class="label label-chicken">
    <div class="brand-tab">COPPER<br>KETTLE<br>BBQ</div>
    <div class="emblem" role="img" aria-label="Emblem of a cow and a chicken"></div>
    <p class="story"><span class="q q-open">“</span>Lorem ipsum dolor sit amet, consectetuer adipiscing elit, sed diam nonummy nibh euismod tincidunt ut laoreet dolore magna aliquam erat volutpat. Ut wisi enim ad minim veniam, quis nostrud exerci tation ullamcorper suscipit lobortis nisl ut aliquip ex ea commodo consequat. Duis autem vel eum iriure dolor in hendrerit in vulputate velit esse molestie consequat, vel illum dolore eu feugiat nulla facilisis at vero eros<span class="q q-close">”</span></p>
    <div class="follow">FOLLOW US ON <span class="dot"></span><span class="dot"></span></div>
    <div class="title" style="top:65px"><span class="dot">■</span>CHICKEN<span class="dot">■</span></div>
    <div class="subtitle" style="top:104px">BARBEQUE RUB</div>
    <div class="animal" role="img" aria-label="White silhouette of a chicken" style="left:188px;top:135px;width:82px;height:86px"></div>
    <div class="rule" style="top:232px"></div>
    <div class="volume" style="top:242px">250ml</div>
    <div class="nutrition">
      <h3>Nutrition Facts</h3>
      <div>1 serving per container</div>
      <div class="row thick"><span>Serving size</span><span>1/4 cup (40g)</span></div>
      <div>Amount per serving</div>
      <div class="cal"><span>Calories</span><span>120</span></div>
      <div class="dv">% Daily Value*</div>
      <div class="row"><span>Total Fat 0g</span><span>0%</span></div>
      <div class="row in"><span>Saturated Fat 0g</span><span>0%</span></div>
      <div class="row in"><span>Trans Fat 0g</span><span></span></div>
      <div class="row"><span>Cholesterol 0mg</span><span>0%</span></div>
      <div class="row"><span>Sodium 10mg</span><span>0%</span></div>
      <div class="row"><span>Total Carbohydrate 32g</span><span>12%</span></div>
      <div class="row in"><span>Dietary Fiber 2g</span><span>7%</span></div>
      <div class="row in"><span>Total Sugars</span><span>26g</span></div>
      <div class="row in"><span>Includes 0 Added Sugars</span><span>0%</span></div>
      <div class="row thick"><span>Protein 1g</span><span></span></div>
      <div class="row"><span>Vitamin D 0mcg</span><span>0%</span></div>
      <div class="row"><span>Calcium 25mg</span><span>2%</span></div>
      <div class="row"><span>Iron 0.7mg</span><span>4%</span></div>
      <div class="row"><span>Potassium 298mg</span><span>6%</span></div>
      <div class="foot">The % Daily Value tells you how much a nutrient in a serving adds to a daily diet.<br><b>Ingredients:</b> Salt, Pepper, Garlic</div>
    </div>
  </article>

  <article class="label label-pig">
    <div class="brand-tab">COPPER<br>KETTLE<br>BBQ</div>
    <div class="emblem" role="img" aria-label="Emblem of a cow and a chicken" style="top:36px"></div>
    <p class="story" style="top:98px"><span class="q q-open">“</span>Lorem ipsum dolor sit amet, consectetuer adipiscing elit, sed diam nonummy nibh euismod tincidunt ut laoreet dolore magna aliquam erat volutpat. Ut wisi enim ad minim veniam, quis nostrud exerci tation ullamcorper suscipit lobortis nisl ut aliquip ex ea commodo consequat. Duis autem vel eum iriure dolor in hendrerit in vulputate velit esse molestie consequat, vel illum dolore eu feugiat nulla facilisis at vero eros<span class="q q-close">”</span></p>
    <div class="follow">FOLLOW US ON <span class="dot"></span><span class="dot"></span></div>
    <div class="title" style="top:98px"><span class="dot">■</span>PIG<span class="dot">■</span></div>
    <div class="subtitle" style="top:136px">BARBEQUE RUB</div>
    <div class="animal" role="img" aria-label="White silhouette of a pig" style="left:168px;top:180px;width:106px;height:60px"></div>
    <div class="rule" style="top:262px"></div>
    <div class="volume" style="top:270px">250ml</div>
    <div class="nutrition" style="top:50px">
      <h3>Nutrition Facts</h3>
      <div>1 serving per container</div>
      <div class="row thick"><span>Serving size</span><span>1/4 cup (40g)</span></div>
      <div>Amount per serving</div>
      <div class="cal"><span>Calories</span><span>120</span></div>
      <div class="dv">% Daily Value*</div>
      <div class="row"><span>Total Fat 0g</span><span>0%</span></div>
      <div class="row in"><span>Saturated Fat 0g</span><span>0%</span></div>
      <div class="row in"><span>Trans Fat 0g</span><span></span></div>
      <div class="row"><span>Cholesterol 0mg</span><span>0%</span></div>
      <div class="row"><span>Sodium 10mg</span><span>0%</span></div>
      <div class="row"><span>Total Carbohydrate 32g</span><span>12%</span></div>
      <div class="row in"><span>Dietary Fiber 2g</span><span>7%</span></div>
      <div class="row in"><span>Total Sugars</span><span>26g</span></div>
      <div class="row in"><span>Includes 0 Added Sugars</span><span>0%</span></div>
      <div class="row thick"><span>Protein 1g</span><span></span></div>
      <div class="row"><span>Vitamin D 0mcg</span><span>0%</span></div>
      <div class="row"><span>Calcium 25mg</span><span>2%</span></div>
      <div class="row"><span>Iron 0.7mg</span><span>4%</span></div>
      <div class="row"><span>Potassium 298mg</span><span>6%</span></div>
      <div class="foot">The % Daily Value tells you how much a nutrient in a serving adds to a daily diet.<br><b>Ingredients:</b> Salt, Pepper, Garlic</div>
    </div>
  </article>

  <article class="label label-beef">
    <div class="brand-tab">COPPER<br>KETTLE<br>BBQ</div>
    <div class="emblem" role="img" aria-label="Emblem of a cow and a chicken" style="top:36px"></div>
    <p class="story" style="top:96px"><span class="q q-open">“</span>Lorem ipsum dolor sit amet, consectetuer adipiscing elit, sed diam nonummy nibh euismod tincidunt ut laoreet dolore magna aliquam erat volutpat. Ut wisi enim ad minim veniam, quis nostrud exerci tation ullamcorper suscipit lobortis nisl ut aliquip ex ea commodo consequat. Duis autem vel eum iriure dolor in hendrerit in vulputate velit esse molestie consequat, vel illum dolore eu feugiat nulla facilisis at vero eros<span class="q q-close">”</span></p>
    <div class="follow">FOLLOW US ON <span class="dot"></span><span class="dot"></span></div>
    <div class="title" style="top:96px"><span class="dot">■</span>BEEF<span class="dot">■</span></div>
    <div class="subtitle" style="top:134px">BARBEQUE RUB</div>
    <div class="animal" role="img" aria-label="White silhouette of a cow" style="left:180px;top:180px;width:90px;height:68px"></div>
    <div class="rule" style="top:262px"></div>
    <div class="volume" style="top:270px">250ml</div>
    <div class="nutrition" style="top:50px">
      <h3>Nutrition Facts</h3>
      <div>1 serving per container</div>
      <div class="row thick"><span>Serving size</span><span>1/4 cup (40g)</span></div>
      <div>Amount per serving</div>
      <div class="cal"><span>Calories</span><span>120</span></div>
      <div class="dv">% Daily Value*</div>
      <div class="row"><span>Total Fat 0g</span><span>0%</span></div>
      <div class="row in"><span>Saturated Fat 0g</span><span>0%</span></div>
      <div class="row in"><span>Trans Fat 0g</span><span></span></div>
      <div class="row"><span>Cholesterol 0mg</span><span>0%</span></div>
      <div class="row"><span>Sodium 10mg</span><span>0%</span></div>
      <div class="row"><span>Total Carbohydrate 32g</span><span>12%</span></div>
      <div class="row in"><span>Dietary Fiber 2g</span><span>7%</span></div>
      <div class="row in"><span>Total Sugars</span><span>26g</span></div>
      <div class="row in"><span>Includes 0 Added Sugars</span><span>0%</span></div>
      <div class="row thick"><span>Protein 1g</span><span></span></div>
      <div class="row"><span>Vitamin D 0mcg</span><span>0%</span></div>
      <div class="row"><span>Calcium 25mg</span><span>2%</span></div>
      <div class="row"><span>Iron 0.7mg</span><span>4%</span></div>
      <div class="row"><span>Potassium 298mg</span><span>6%</span></div>
      <div class="foot">The % Daily Value tells you how much a nutrient in a serving adds to a daily diet.<br><b>Ingredients:</b> Salt, Pepper, Garlic</div>
    </div>
  </article>
</main>
</body>
</html>
```